Brightstep Dance Business Card

I'm looking for a two-sided business card design to promote my country dance busness. Cowboy hats, boots, and wood grain floor textures, are all appropriate to use.
On one side I want it to say:
Brightstep Dance
with
Mark
Take The Challenge - Experience The Growth
210-555-0143
On the other side I want:
A place for a Head Shot
The Quote: Experience Is The Best Teacher
A two column bullet list with the following:
First column: Two Step, Waltz, Triple Two, Polka
Second column: Cha-Cha, West Coast, East Cost, NightClub
My Name: Mark Delway
My Phone Number: 210-555-0143

```html
<!DOCTYPE html>
<html lang="en">
<head>
<meta charset="utf-8">
<title>Brightstep Dance Business Card</title>
<link rel="stylesheet" href="https://fonts.googleapis.com/css2?family=Norican&family=Montserrat:wght@400;500;600;800&family=Oswald:wght@600&display=swap">
<style>
  :root {
    --page: #d4d4d6;
    --card: #f5f1e6;
    --card-edge: #ece6d6;
    --ink: #141414;
    --rule: #3a3a3a;
    --photo: #9b9b9b;
    --photo-dark: #6e6e6e;
  }
  * { box-sizing: border-box; margin: 0; padding: 0; }
  html, body { width: 1200px; height: 800px; overflow: hidden; }
  body {
    background: var(--page);
    display: flex; flex-direction: column; align-items: center; justify-content: center;
    gap: 28px;
    font-family: "Montserrat", sans-serif;
    color: var(--ink);
  }
  .card {
    position: relative;
    width: 630px; height: 360px;
    border-radius: 22px;
    overflow: hidden;
    box-shadow: 0 6px 16px rgba(0,0,0,.18);
  }
  .card-texture {
    position: absolute; inset: 0;
    background: radial-gradient(circle at 40% 45%, var(--card) 0%, var(--card-edge) 100%);
  }
  /* Front */
  .front-content {
    position: relative; height: 100%;
    display: flex; flex-direction: column; align-items: center; justify-content: center;
    text-align: center;
  }
  .studio-name { font-family: "Norican", cursive; font-size: 58px; line-height: 1; }
  .with-rule {
    display: flex; align-items: center; gap: 10px;
    width: 400px; margin: 10px 0 2px;
    font-size: 13px; letter-spacing: 2px; font-weight: 500;
  }
  .with-rule::before, .with-rule::after { content: ""; flex: 1; height: 1px; background: var(--rule); }
  .teacher-name { font-size: 76px; font-weight: 500; letter-spacing: 4px; line-height: 1; }
  .tagline { font-size: 15px; font-weight: 600; letter-spacing: 1.5px; text-transform: uppercase; line-height: 1.35; margin-top: 8px; }
  .phone { display: flex; align-items: center; gap: 8px; font-family: "Oswald", sans-serif; font-weight: 600; }
  .front-content .phone { font-size: 30px; margin-top: 8px; }
  .phone svg { flex: none; }
  /* Back */
  .back-content { position: relative; height: 100%; }
  .headshot {
    position: absolute; left: 40px; top: 58px; width: 200px; height: 220px;
    background: linear-gradient(180deg, var(--photo) 0%, var(--photo-dark) 100%);
  }
  .signature-name {
    position: absolute; left: 30px; top: 284px; width: 220px; text-align: center;
    font-family: "Norican", cursive; font-size: 34px;
  }
  .back-info { position: absolute; left: 268px; top: 36px; width: 330px; }
  .quote { text-transform: uppercase; font-weight: 800; line-height: 1; }
  .quote-lead { font-size: 24px; font-weight: 600; display: block; }
  .quote-main { font-size: 36px; display: block; }
  .divider { height: 1.5px; background: var(--rule); margin: 12px 0; }
  .styles { display: grid; grid-template-columns: 1fr 1fr; column-gap: 14px; list-style: none; }
  .styles ul { list-style: none; }
  .styles li { display: flex; align-items: center; gap: 7px; font-size: 17px; line-height: 1.45; }
  .back-info .phone { font-size: 42px; }
</style>
</head>
<body>

<section class="card card-front" aria-label="Card front">
  <div class="card-texture" role="img" aria-label="Faint western pattern of boots, hats, horseshoes, cacti and sheriff stars on cream"></div>
  <div class="front-content">
    <h1 class="studio-name">Brightstep Dance</h1>
    <div class="with-rule">WITH</div>
    <p class="teacher-name">MARK</p>
    <p class="tagline">Take the challenge<br>Experience the growth</p>
    <p class="phone">
      <svg width="30" height="26" viewBox="0 0 30 26" aria-hidden="true"><path d="M4 8c0-3 4-5 11-5s11 2 11 5v2h-6V7.5C18 7 12 7 10 7.5V10H4z M9 12h12l4 9H5z" fill="none" stroke="currentColor" stroke-width="2" stroke-linejoin="round"/></svg>
      210-555-0143
    </p>
  </div>
</section>

<section class="card card-back" aria-label="Card back">
  <div class="card-texture" role="img" aria-label="Faint western pattern of boots, hats, horseshoes, cacti and sheriff stars on cream"></div>
  <div class="back-content">
    <div class="headshot" role="img" aria-label="Head shot of Mark Delway"></div>
    <p class="signature-name">Mark Delway</p>
    <div class="back-info">
      <h2 class="quote"><span class="quote-lead">Experience is the</span><span class="quote-main">Best Teacher</span></h2>
      <div class="divider"></div>
      <div class="styles">
        <ul>
          <li><svg width="16" height="16" viewBox="0 0 16 16" aria-hidden="true"><rect x="1" y="1" width="14" height="14" fill="none" stroke="currentColor" stroke-width="2"/><path d="M4 8l3 3 6-7" fill="none" stroke="currentColor" stroke-width="2.2"/></svg>Two Step</li>
          <li><svg width="16" height="16" viewBox="0 0 16 16" aria-hidden="true"><rect x="1" y="1" width="14" height="14" fill="none" stroke="currentColor" stroke-width="2"/><path d="M4 8l3 3 6-7" fill="none" stroke="currentColor" stroke-width="2.2"/></svg>Waltz</li>
          <li><svg width="16" height="16" viewBox="0 0 16 16" aria-hidden="true"><rect x="1" y="1" width="14" height="14" fill="none" stroke="currentColor" stroke-width="2"/><path d="M4 8l3 3 6-7" fill="none" stroke="currentColor" stroke-width="2.2"/></svg>Triple Two</li>
          <li><svg width="16" height="16" viewBox="0 0 16 16" aria-hidden="true"><rect x="1" y="1" width="14" height="14" fill="none" stroke="currentColor" stroke-width="2"/><path d="M4 8l3 3 6-7" fill="none" stroke="currentColor" stroke-width="2.2"/></svg>Polka</li>
        </ul>
        <ul>
          <li><svg width="16" height="16" viewBox="0 0 16 16" aria-hidden="true"><rect x="1" y="1" width="14" height="14" fill="none" stroke="currentColor" stroke-width="2"/><path d="M4 8l3 3 6-7" fill="none" stroke="currentColor" stroke-width="2.2"/></svg>Cha-Cha</li>
          <li><svg width="16" height="16" viewBox="0 0 16 16" aria-hidden="true"><rect x="1" y="1" width="14" height="14" fill="none" stroke="currentColor" stroke-width="2"/><path d="M4 8l3 3 6-7" fill="none" stroke="currentColor" stroke-width="2.2"/></svg>West Coast</li>
          <li><svg width="16" height="16" viewBox="0 0 16 16" aria-hidden="true"><rect x="1" y="1" width="14" height="14" fill="none" stroke="currentColor" stroke-width="2"/><path d="M4 8l3 3 6-7" fill="none" stroke="currentColor" stroke-width="2.2"/></svg>East Cost</li>
          <li><svg width="16" height="16" viewBox="0 0 16 16" aria-hidden="true"><rect x="1" y="1" width="14" height="14" fill="none" stroke="currentColor" stroke-width="2"/><path d="M4 8l3 3 6-7" fill="none" stroke="currentColor" stroke-width="2.2"/></svg>NightClub</li>
        </ul>
      </div>
      <div class="divider"></div>
      <p class="phone">
        <svg width="38" height="32" viewBox="0 0 30 26" aria-hidden="true"><path d="M4 8c0-3 4-5 11-5s11 2 11 5v2h-6V7.5C18 7 12 7 10 7.5V10H4z M9 12h12l4 9H5z" fill="none" stroke="currentColor" stroke-width="2" stroke-linejoin="round"/></svg>
        210-555-0143
      </p>
    </div>
  </div>
</section>

</body>
</html>
```